Business Card Design for a Lending Business (Hard Money loans)

We need a business card for our Real Estate Lending business. We do hard Money loans for real estate investors. We have an existing logo we like, see attached. I'd like the business card to mostly include the logo colors, but a bright color pop of some sort would be nice to see also. Card should include Logo, Company Name, Company Address, Employee Name, Cell Phone, Main Phone, Email, Website

Industry/Entity Type

Finance / Lending

Contact Information for Business Card

Logo, Company Name, Company Address, Employee Name, Cell Phone, Main Phone, Email, Website

Requirements
Nice to have
• I'd like the business card to mostly include the logo colors, but a bright color pop of some sort would be nice to see also.

```html
<!DOCTYPE html>
<html lang="en">
<head>
<meta charset="utf-8">
<title>Northgate Lending – Business Card</title>
<link rel="stylesheet" href="https://fonts.googleapis.com/css2?family=Montserrat:wght@600;700&family=Open+Sans:wght@400&display=swap">
<style>
  :root {
    --navy: #2a3683;
    --cyan: #0aa7dc;
    --ink: #444448;
    --paper: #ffffff;
    --backdrop: #d6d6d6;
  }
  * { box-sizing: border-box; margin: 0; padding: 0; }
  html, body { width: 1200px; height: 896px; overflow: hidden; }
  body { background: var(--backdrop); position: relative; font-family: "Open Sans", sans-serif; }

  .card {
    position: absolute;
    left: 334px;
    width: 527px;
    height: 301px;
    border-radius: 24px;
    overflow: hidden;
  }
  .card--front { top: 125px; background: var(--paper); }
  .card--back { top: 474px; background: var(--navy); }

  .wave { position: absolute; left: 0; top: 0; width: 527px; height: 301px; }

  .brand {
    position: absolute;
    font-family: "Montserrat", sans-serif;
    font-weight: 700;
    text-align: center;
    letter-spacing: 0.12em;
    line-height: 1.15;
  }
  .card--front .brand {
    left: 40px; width: 210px; top: 112px;
    color: var(--navy);
    font-size: 24px;
  }
  .brand__mark {
    display: block;
    margin: 0 auto 12px;
    border-radius: 50%;
    background: var(--cyan);
  }
  .card--front .brand__mark { width: 26px; height: 26px; }

  .divider {
    position: absolute;
    left: 259px; top: 77px;
    width: 1.5px; height: 145px;
    background: var(--cyan);
  }

  .contact { position: absolute; left: 276px; top: 72px; color: var(--ink); }
  .contact__name {
    font-family: "Montserrat", sans-serif;
    font-weight: 700;
    font-size: 18px;
    color: var(--cyan);
    line-height: 24px;
  }
  .contact__title { font-size: 14px; line-height: 20px; }
  .contact__address { font-size: 14px; line-height: 19px; margin-top: 8px; }
  .contact__list { list-style: none; margin-top: 12px; font-size: 13px; }
  .contact__list li { display: flex; align-items: center; height: 19px; }
  .contact__list svg { width: 12px; height: 12px; margin-right: 7px; fill: var(--cyan); }

  .website {
    position: absolute;
    right: 22px; top: 267px;
    color: var(--paper);
    font-size: 14px;
    line-height: 18px;
  }

  .card--back .brand {
    left: 0; width: 527px; top: 86px;
    color: var(--paper);
    font-size: 38px;
  }
  .card--back .brand__mark { width: 40px; height: 40px; margin-bottom: 18px; background: var(--paper); }
</style>
</head>
<body>

<section class="card card--front" aria-label="Business card front">
  <svg class="wave" viewBox="0 0 527 301" aria-hidden="true">
    <path fill="var(--cyan)" d="M90 292 C200 292 330 236 527 230 L527 247 C330 252 270 277 230 291 C180 297 130 296 90 292 Z"/>
    <path fill="var(--navy)" d="M0 272 C80 295 160 300 230 294 C270 280 330 255 527 250 L527 301 L0 301 Z"/>
  </svg>

  <div class="brand">
    <span class="brand__mark"></span>
    NORTHGATE<br>LENDING
  </div>

  <div class="divider"></div>

  <div class="contact">
    <p class="contact__name">DANA WHITFIELD</p>
    <p class="contact__title">Managing Director</p>
    <p class="contact__address">214 Alder Court, Suite 302<br>Lakewood, CO 80226</p>
    <ul class="contact__list">
      <li>
        <svg viewBox="0 0 24 24"><path d="M6.6 10.8a15.1 15.1 0 0 0 6.6 6.6l2.2-2.2a1 1 0 0 1 1-.25 11.4 11.4 0 0 0 3.6.57 1 1 0 0 1 1 1V20a1 1 0 0 1-1 1A17 17 0 0 1 3 4a1 1 0 0 1 1-1h3.5a1 1 0 0 1 1 1c0 1.25.2 2.45.57 3.57a1 1 0 0 1-.25 1z"/></svg>
        303 555 0148
      </li>
      <li>
        <svg viewBox="0 0 24 24"><path d="M7 1h10a2 2 0 0 1 2 2v18a2 2 0 0 1-2 2H7a2 2 0 0 1-2-2V3a2 2 0 0 1 2-2zm0 3v14h10V4zm5 15.5a1.2 1.2 0 1 0 0 2.4 1.2 1.2 0 0 0 0-2.4z"/></svg>
        303 555 0192
      </li>
      <li>
        <svg viewBox="0 0 24 24"><path d="M2 5h20v2l-10 6L2 7zm0 4.3 10 6 10-6V19H2z"/></svg>
        info@northgatelending.com
      </li>
    </ul>
  </div>

  <p class="website">www.northgatelending.com</p>
</section>

<section class="card card--back" aria-label="Business card back">
  <div class="brand">
    <span class="brand__mark"></span>
    NORTHGATE<br>LENDING
  </div>
</section>

</body>
</html>
```